Lifecoach needs website design based on a standard Wordpress theme

I need a website for my new lifecoaching business that can be easily implemented in Wordpress, it needs to be compatible with a standard Wordpress theme. So I can place the pictures, texts etc. in a standard theme of Wordpress.

I want the design to be a very good feeling and playfull one, based on my logo.

Target Market(s)

I will coach people to reach their goals and dreams in life.

Industry/Entity Type

Business

Requirements
Must have
• Can be easy implemented in Wordpress.
Nice to have
• Photo's of nature are nice.

```html
<!DOCTYPE html>
<html lang="en">
<head>
<meta charset="utf-8">
<title>Mara Linden Lifecoach</title>
<link href="https://fonts.googleapis.com/css2?family=Source+Sans+3:wght@400;600;700&family=Ubuntu:wght@300;400&display=swap" rel="stylesheet">
<style>
:root{
  --blue:#2e8fd6;
  --blue-dark:#1f74b8;
  --navy:#0a4570;
  --navy-text:#144a7a;
  --cyan:#0fb0ea;
  --orange:rgba(255,133,52,.88);
  --grey-text:#8a8f96;
  --line:#d9dde1;
  --page:#f8fafb;
  --gold:#f0b429;
}
*{box-sizing:border-box;margin:0;padding:0}
html,body{width:933px;height:1200px;overflow:hidden}
body{position:relative;background:var(--page);font-family:"Ubuntu",sans-serif;color:var(--grey-text)}
.abs{position:absolute}
.topbar{left:0;top:0;width:933px;height:51px;background:#fff}
.contact-top{top:20px;font-size:8px;color:var(--blue-dark);display:flex;align-items:center;gap:5px}
.navband{left:0;top:51px;width:933px;height:36px;background:linear-gradient(#47a6e6,var(--blue))}
.nav{left:476px;top:51px;height:36px;display:flex}
.nav a{display:flex;align-items:center;justify-content:center;height:36px;color:#fff;font:600 10px "Source Sans 3",sans-serif;text-decoration:none;border-left:1px solid #1f6fae}
.nav a:last-child{border-right:1px solid #1f6fae}
.nav a.active{background:#2a7cc0}
.hero{left:0;top:87px;width:933px;height:551px;background:linear-gradient(180deg,#b6d8f0 0%,#e7f1f8 45%,#c9b98a 75%,#d67a3a 100%)}
.logo{left:124px;top:0;width:292px;height:109px;background:linear-gradient(#fafafa,#ececec);border-radius:0 0 4px 4px;box-shadow:0 2px 4px rgba(0,0,0,.15);display:flex;align-items:center;padding-left:20px;gap:10px}
.logo-mark{width:60px;height:60px;border-radius:50%;border:4px solid var(--blue-dark)}
.logo-name{font:600 19px/1.1 "Source Sans 3",sans-serif;color:var(--navy-text)}
.promo{left:0;top:224px;width:454px;height:189px;background:var(--orange);padding:33px 40px 0 136px;color:#fff}
.promo h1{font:700 26px/1.25 "Source Sans 3",sans-serif;text-shadow:0 1px 2px rgba(0,0,0,.15)}
.promo p{font:300 12.5px/1.3 "Ubuntu",sans-serif;margin-top:9px;padding-left:3px}
.card{top:518px;width:219px;height:264px;background:#fff;border:1px solid #d7dadd;padding:0 11px}
.card h2{font:400 17.5px "Source Sans 3",sans-serif;color:var(--navy-text);text-align:center;margin-top:14px;height:24px}
.card .photo{width:197px;height:102px;margin-top:3px}
.card p{font-size:8.5px;line-height:1.7;margin-top:12px}
.btn{display:inline-flex;align-items:center;gap:5px;height:27px;padding:0 15px;border:1px solid #c9cdd1;border-radius:14px;background:linear-gradient(#fff,#ececec);font-size:8.5px;color:#8a8f96}
.card .btn{margin-top:16px}
.field{height:27px;border:1px solid var(--gold);font-size:8px;color:#5c6670;padding:9px 10px;margin-top:13px}
.section-title{font:400 17.5px "Source Sans 3",sans-serif;color:var(--navy-text);top:805px}
.rule{top:837px;height:4px;border-top:1px solid var(--line);border-bottom:1px solid var(--line)}
.coach-text{left:360px;top:863px;width:205px;font-size:8.5px;line-height:1.55}
.cta{left:0;top:1052px;width:933px;height:71px;background:var(--cyan);border-top:3px solid #1a8fd0}
.cta-text{left:130px;top:1078px;font:700 17px "Source Sans 3",sans-serif;color:#fff}
.cta-btn{left:633px;top:1071px;width:180px;height:36px;border-radius:5px;background:linear-gradient(#2bb8ee,#109ad8);box-shadow:0 2px 3px rgba(0,0,0,.2);border:1px solid #0d8ac4;display:flex;align-items:center;justify-content:center;color:#fff;font:600 12.5px "Source Sans 3",sans-serif}
.footer{left:0;top:1123px;width:933px;height:77px;background:var(--navy)}
.foot-small{color:#fff;font:600 8px "Source Sans 3",sans-serif}
.social{top:1137px;width:19px;height:19px;border-radius:50%;background:#fff}
</style>
</head>
<body>
<div class="abs topbar"></div>
<div class="abs contact-top" style="left:612px">
  <svg width="22" height="11" viewBox="0 0 22 11"><path d="M8 1h13v9H8z M8 1l6.5 5L21 1 M0 3h6 M2 6h4" fill="none" stroke="#3b8fd0" stroke-width="1"/></svg>
  <span>info@maralinden.com</span>
</div>
<div class="abs contact-top" style="left:733px">
  <svg width="11" height="11" viewBox="0 0 12 12"><path d="M2 1l3 0 1 3-2 1c1 2 2 3 4 4l1-2 3 1v3c-6 0-10-4-10-10z" fill="none" stroke="#3b8fd0" stroke-width="1"/></svg>
  <span>+31 612 345 678</span>
</div>

<div class="abs navband"></div>
<nav class="abs nav">
  <a class="active" style="width:65px">Home</a>
  <a style="width:66px">About</a>
  <a style="width:65px">Coaching</a>
  <a style="width:73px">Articles</a>
  <a style="width:65px">Contact</a>
</nav>

<div class="abs hero" role="img" aria-label="Family playing in a sunny poppy meadow with petals in the air"></div>

<div class="abs logo">
  <div class="logo-mark"></div>
  <div class="logo-name">Mara Linden<br>Lifecoach</div>
</div>

<div class="abs promo">
  <h1>Make your life be what<br>you want it to be!</h1>
  <p>Lorem ipsum dolor sit amet, consectetur adipisic-<br>ing elit, sed do eiusmod tempor incididunt ut<br>labore et dolore magna aliqua.</p>
</div>

<div class="abs card" style="left:124px">
  <h2>What is Life Coaching?</h2>
  <div class="photo" role="img" aria-label="Two women talking in a coaching session" style="background:linear-gradient(90deg,#7a6655,#e9e7e3 50%,#d8cfc4)"></div>
  <p>Lorem ipsum dolor sit amet, consectetur adipisic-ing elit, sed do eiusmod tempor incididunt ut labore et dolore magna aliqua.</p>
  <span class="btn">Read More <span>›</span></span>
</div>
<div class="abs card" style="left:358px">
  <h2>Life Advices</h2>
  <div class="photo" role="img" aria-label="Couple talking outdoors in a green park" style="background:linear-gradient(90deg,#c9ae8f,#8aa84a 50%,#6d8c34)"></div>
  <p>Lorem ipsum dolor sit amet, consectetur adipisic-ing elit, sed do eiusmod tempor incididunt ut labore et dolore magna aliqua.</p>
  <span class="btn">Read More <span>›</span></span>
</div>
<div class="abs card" style="left:590px;padding:0 14px 0 19px">
  <h2>Sign up for Newsletter</h2>
  <p style="margin-top:11px">Lorem ipsum dolor sit amet, consectetur adipisicing elit, sed do eiusmod tempor incididunt ut labore et dolore magna aliqua.</p>
  <div class="field" style="margin-left:-4px">Your Name</div>
  <div class="field" style="margin-left:-4px">Your Email</div>
  <p style="font-size:7.5px;margin-top:9px">*Your email will be held in strictest confidentiality.</p>
  <span class="btn" style="margin-top:22px;margin-left:-4px">Submit Now</span>
</div>

<div class="abs section-title" style="left:128px">Meet Your Life Coach</div>
<div class="abs rule" style="left:126px;width:437px"></div>
<div class="abs section-title" style="left:591px">Client Testimonial</div>
<div class="abs rule" style="left:590px;width:218px"></div>

<div class="abs" role="img" aria-label="Portrait of the life coach smiling" style="left:127px;top:860px;width:217px;height:142px;background:linear-gradient(90deg,#d9d4cd,#b89680 45%,#e8e8e6);border-radius:2px"></div>
<div class="abs coach-text">
  <p>Tempor incididunt ut labore et dolore magna aliqua. Ut enim ad minim veniam, quis nostrud exercitation. Lorem ipsum dolor sit amet, consectetur adipisicing elit, sed do eiusmod</p>
  <p style="margin-top:12px">Lorem ipsum dolor sit amet, consectetur adipisicing elit, sed do eiusmod</p>
  <span class="btn" style="margin-top:20px">Read More <span>›</span></span>
</div>

<div class="abs" role="img" aria-label="Client portrait" style="left:660px;top:852px;width:64px;height:64px;border-radius:50%;background:linear-gradient(#6b4a3a,#c99a80)"></div>
<div class="abs" style="left:590px;top:927px;width:204px;text-align:center">
  <div style="font-size:10px;color:#6c747c">Lena Hart</div>
  <div style="font-size:8.5px;color:#5c6670;margin-top:2px">Lyon, France</div>
</div>
<div class="abs" style="left:600px;top:961px;width:190px;font-size:8.5px;line-height:1.7;font-style:italic;color:#9aa0a6">"Lorem ipsum dolor sit amet, consectetur adipisicing elit, sed do eiusmod tempor incididunt ut labore et dolore magna aliqua."</div>

<div class="abs cta"></div>
<div class="abs cta-text">Life life to the fullest. Book a Private Coaching Session Now.</div>
<div class="abs cta-btn">Request Coaching Session</div>

<div class="abs footer"></div>
<div class="abs foot-small" style="left:131px;top:1142px">LINKS &nbsp;| &nbsp;LINKS &nbsp;| &nbsp;LINKS &nbsp;| &nbsp;LINKS</div>
<div class="abs foot-small" style="left:130px;top:1165px;font-weight:400">Copyright © 2014. All rights reserved. &nbsp;Company Name. Privacy Policy &nbsp;| &nbsp;Sitemap</div>
<div class="abs social" style="left:539px"></div>
<div class="abs social" style="left:568px"></div>
<div class="abs social" style="left:597px"></div>
<div class="abs" style="left:652px;top:1139px;display:flex;align-items:center;gap:13px">
  <svg width="14" height="10" viewBox="0 0 14 10"><rect width="14" height="10" fill="#2e8fd6"/><path d="M0 0l7 5 7-5" fill="none" stroke="#0a4570" stroke-width="1"/></svg>
  <span class="foot-small">hello@maralinden.com</span>
</div>
<div class="abs" style="left:652px;top:1161px;display:flex;align-items:center;gap:13px">
  <svg width="13" height="13" viewBox="0 0 12 12"><path d="M2 1l3 0 1 3-2 1c1 2 2 3 4 4l1-2 3 1v3c-6 0-10-4-10-10z" fill="#2e8fd6"/></svg>
  <span class="foot-small">020-555-0147</span>
</div>
</body>
</html>
```